Tillard Environmental Projects New Website Design

I need a new website for a Environmental Project Company based in Sydney Australia, working throughout South East Asia.I've attached the company logo, please try & incorporate these colours or use complimentary colours. I've attached a word doc with design brief.I'm going to use Wix, so please ensure files are suitable.Thankyou.

Number of Pages Required

5+ page

Colors

Designer to choose colors to be used in the design.

Requirements
Must have
• Refer to Word Document
Nice to have
• Refer to Word Document
Should not have
• Not to be dark

```html
<!DOCTYPE html>
<html lang="en">
<head>
<meta charset="utf-8">
<title>Tillard Environmental Projects</title>
<link href="https://fonts.googleapis.com/css2?family=Exo+2:wght@300;400;600;700&family=Open+Sans:wght@400;600&display=swap" rel="stylesheet">
<style>
:root{
  --green:#7cc10c;
  --green-dark:#3d5a10;
  --forest:#1c2a08;
  --teal:#1aa79a;
  --orange:#fe5722;
  --text:#333;
  --muted:#888;
  --white:#fff;
}
*{margin:0;padding:0;box-sizing:border-box}
html,body{width:1200px;height:1200px;overflow:hidden;background:#fff}
body{font-family:"Open Sans",sans-serif;color:var(--text)}
.page{position:absolute;left:282px;top:0;width:793px;height:1500px;transform:scale(.8);transform-origin:0 0;background:#fff;overflow:hidden}
.abs{position:absolute}
.head{font-family:"Exo 2",sans-serif}

/* nav */
.topbar{left:0;top:0;width:793px;height:38px;border-top:2px solid var(--teal);background:#fff}
.brand{left:106px;top:6px;display:flex;align-items:center;gap:5px;font-family:"Exo 2",sans-serif;font-size:8px;font-weight:600;color:var(--green-dark);line-height:1.1;width:120px}
.brand .dot{width:26px;height:26px;border-radius:50%;background:var(--green-dark);flex:none}
.nav{left:288px;top:0;display:flex;height:36px;font-size:8px;text-transform:uppercase}
.nav a{display:block;padding:0 12px;line-height:36px;color:#333;text-decoration:none;margin-right:6px}
.nav a.active{background:var(--teal);color:#fff;font-weight:600}

/* hero */
.hero{left:0;top:38px;width:793px;height:344px;background:linear-gradient(120deg,#4a3a2e 0%,#6b4f3a 35%,#3e3024 60%,#5c4430 100%)}
.hero-shade{left:0;top:38px;width:793px;height:344px;background:rgba(0,0,0,.3)}
.hero h1{left:0;top:106px;width:793px;text-align:center;font-family:"Exo 2",sans-serif;line-height:26px}
.hero-l1{display:block;font-weight:300;font-size:29px;color:#fff}
.hero-l2{display:block;font-weight:700;font-size:28px;color:var(--green)}
.hero-copy{left:180px;top:175px;width:433px;text-align:center;font-size:7.5px;color:#eee;line-height:10px}
.btn-contact{left:348px;top:209px;width:97px;height:22px;border-radius:11px;background:var(--green);border:2px solid #5a9a06;color:#fff;font-size:8.5px;font-weight:600;display:flex;align-items:center;justify-content:center;gap:6px}
.arrow{top:197px;width:24px;height:24px;border-radius:50%;background:rgba(255,255,255,.15);color:#ddd;font-size:12px;text-align:center;line-height:23px}

.feature{top:270px;width:194px;height:112px;text-align:center;color:#fff;background:rgba(62,95,20,.88)}
.feature.teal{background:var(--teal)}
.feature svg{margin-top:14px}
.feature h3{font-family:"Exo 2",sans-serif;font-weight:400;font-size:12px;margin-top:4px}
.feature p{font-size:7px;line-height:10px;color:#e3eedd;margin:6px 18px 0}

/* about */
.field{left:0;top:382px;width:793px;height:296px;background:linear-gradient(180deg,#6ba41a 0%,#4c8a1c 30%,#2f5f14 55%,#1f3b0c 100%)}
.about-band{left:0;top:544px;width:793px;height:134px;background:rgba(26,42,10,.75)}
.about-title{left:0;top:558px;width:793px;text-align:center;font-family:"Exo 2",sans-serif;font-weight:700;font-size:24px;color:var(--green)}
.about-rule{left:387px;top:590px;width:19px;height:2px;background:var(--green)}
.about-rule-thin{left:347px;top:591px;width:100px;height:1px;background:rgba(255,255,255,.15)}
.statement{top:608px;width:280px}
.statement h4{font-family:"Exo 2",sans-serif;font-weight:400;font-size:12px;color:var(--green)}
.statement p{font-size:7px;line-height:10px;color:#e5e5e5;margin-top:8px}
.about-divider{left:398px;top:612px;width:1px;height:46px;background:rgba(255,255,255,.15)}

/* section titles */
.section-title{left:0;width:793px;display:flex;align-items:center;justify-content:center;gap:8px;font-family:"Exo 2",sans-serif;font-weight:700;font-size:22px;color:var(--green-dark)}
.section-title .line{width:114px;height:2px;background:var(--green-dark)}

/* products */
.tile{overflow:hidden}
.tile-text{text-align:center;color:#fff}
.tile-text h3{font-family:"Exo 2",sans-serif;font-weight:400;font-size:17px;margin-top:36px}
.tile-text .bar{width:16px;height:2px;background:#fff;margin:8px auto 10px}
.tile-text p{font-size:7.3px;line-height:11px;margin:0 16px}
.play{left:177px;top:866px;width:40px;height:40px}

/* blog */
.post{top:1102px;width:181px}
.post .thumb{width:181px;height:115px}
.post .meta{font-size:7px;color:var(--muted);margin-top:8px;display:flex;gap:10px}
.post h4{font-size:8.5px;font-weight:400;line-height:12px;margin-top:8px;text-decoration:underline;color:#222;text-transform:uppercase}

/* footer */
.footer{left:0;top:1289px;width:793px;height:211px;background:var(--forest)}
.f-brand{left:106px;top:1335px;display:flex;align-items:center;gap:8px;font-family:"Exo 2",sans-serif;font-size:13px;color:var(--green-dark);line-height:14px;width:160px}
.f-brand .dot{width:50px;height:50px;border-radius:50%;background:#2c4210;flex:none}
.social{top:1414px;width:22px;height:22px;border:1px solid var(--teal);border-radius:2px}
.f-title{font-family:"Exo 2",sans-serif;font-weight:400;font-size:15px;color:var(--teal)}
.links{left:353px;top:1346px;list-style:none;font-size:8px;color:#ddd}
.links li{height:20px;display:flex;align-items:center;gap:7px}
.links li::before{content:"";width:5px;height:5px;border:1px solid var(--teal);border-radius:50%}
.field-input{left:522px;width:168px;height:23px;border:1px solid #445a2c;border-radius:3px;background:#22300f;font-size:7px;color:#ccc;padding-left:18px;line-height:21px}
.subscribe{left:522px;top:1408px;width:168px;height:22px;background:var(--teal);border-radius:3px;color:#fff;font-size:9px;text-align:center;line-height:22px;text-transform:uppercase}
.copy-line{left:0;top:1471px;width:793px;height:1px;background:#2d3d18}
.copyright{left:0;top:1480px;width:793px;text-align:center;font-size:7.5px;color:#ccc}
</style>
</head>
<body>
<div class="page">

  <header class="abs topbar"></header>
  <div class="abs brand"><span class="dot"></span><span>TILLARD ENVIRONMENTAL PROJECTS</span></div>
  <nav class="abs nav">
    <a class="active">Home</a><a>Who we are</a><a>Services</a><a>Products</a><a>News</a><a>Contact</a>
  </nav>

  <div class="abs hero" role="img" aria-label="Hands planting a seedling in rich soil"></div>
  <div class="abs hero-shade"></div>
  <h1 class="abs hero"><span class="hero-l1">INVESTING IN GREEN</span><span class="hero-l2">INFRASTRUCTURE &amp; PROJECTS.</span></h1>
  <p class="abs hero-copy">Lorem Ipsum is simply dummy text of the printing and typesetting industry. Lorem Ipsum has been the industry's standard dummy text ever since the 1500s, when an unknown printer took a galley...</p>
  <div class="abs btn-contact">
    <svg width="11" height="8" viewBox="0 0 11 8"><rect x=".5" y=".5" width="10" height="7" fill="none" stroke="#fff"/><path d="M.5 .5 5.5 4.5 10.5 .5" fill="none" stroke="#fff"/></svg>
    CONTACT US
  </div>
  <div class="abs arrow" style="left:9px">«</div>
  <div class="abs arrow" style="left:754px;background:none">»</div>

  <div class="abs feature" style="left:106px">
    <svg width="24" height="32" viewBox="0 0 24 32" fill="none" stroke="#fff" stroke-width="1.3"><path d="M12 4v26M6 12v18M18 12v18"/><path d="M12 8l-3-3M12 8l3-3M12 14l-3-3M12 14l3-3M6 16l-2-2M6 16l2-2M18 16l-2-2M18 16l2-2"/></svg>
    <h3>Sustainable Food</h3>
    <p>Lorem Ipsum is simply dummy text of the printing and typesetting industry...</p>
  </div>
  <div class="abs feature teal" style="left:299px">
    <svg width="28" height="32" viewBox="0 0 28 32" fill="none" stroke="#fff" stroke-width="1.4"><path d="M14 3c-5 8-7 11-7 15a7 7 0 0 0 14 0c0-4-2-7-7-15z" fill="#fff"/><path d="M2 28q12 6 24 0"/></svg>
    <h3>Water quality &amp; treatment</h3>
    <p>Lorem Ipsum is simply dummy text of the printing and typesetting industry...</p>
  </div>
  <div class="abs feature" style="left:493px">
    <svg width="30" height="32" viewBox="0 0 30 32" fill="none" stroke="#fff" stroke-width="1.4"><path d="M3 16 15 6l12 10M7 13v14h16V13"/><path d="M10 20q5-4 10 0M10 24q5-4 10 0"/></svg>
    <h3>Air Quality</h3>
    <p>Lorem Ipsum is simply dummy text of the printing and typesetting industry...</p>
  </div>

  <div class="abs field" role="img" aria-label="Person tending rows of leafy vegetables in a green field"></div>
  <div class="abs about-band"></div>
  <h2 class="abs about-title">ABOUT US</h2>
  <div class="abs about-rule-thin"></div>
  <div class="abs about-rule"></div>
  <div class="abs statement" style="left:106px">
    <h4>Vision Statement:</h4>
    <p>Our Vision is to make it easy for everyone to minimise their environmental impact by providing information, technology, packaged green solutions &amp; helping innovation flourish.</p>
  </div>
  <div class="abs about-divider"></div>
  <div class="abs statement" style="left:415px">
    <h4>Mission Statement:</h4>
    <p>Working with people to minimise the environmental impact of humans on the earth without sacrificing lifestyle and helping innovation flourish.</p>
  </div>

  <h2 class="abs section-title" style="top:692px"><span class="line"></span>OUR PRODUCTS<span class="line"></span></h2>

  <div class="abs tile" style="left:0;top:731px;width:394px;height:310px;background:linear-gradient(180deg,#b9c2c8 0%,#9aa6ab 25%,#4f6b3a 45%,#3d5a28 75%,#5a6e3a 100%)" role="img" aria-label="Video still of large dome greenhouses set among gardens"></div>
  <svg class="abs play" viewBox="0 0 40 40"><circle cx="20" cy="20" r="18" fill="rgba(255,255,255,.2)" stroke="#fff" stroke-width="2.5"/><path d="M16 13v14l11-7z" fill="#fff"/></svg>

  <div class="abs tile tile-text" style="left:394px;top:731px;width:199px;height:148px;background:var(--green)">
    <h3>GREEN WALLS</h3><div class="bar"></div>
    <p>Lorem Ipsum is simply dummy text of the printing and typesetting industry. Lorem Ipsum has been the industry's standard dummy text ever since the 1500s...</p>
  </div>
  <svg class="abs" style="left:486px;top:878px" width="14" height="8" viewBox="0 0 14 8"><path d="M0 0h14L7 7z" fill="#7cc10c"/></svg>
  <div class="abs tile" style="left:593px;top:731px;width:200px;height:148px;background:linear-gradient(135deg,#7ea64a,#c9d9b8 50%,#6d9a3a)" role="img" aria-label="Rows of lettuce growing in a hydroponic frame"></div>
  <div class="abs tile" style="left:394px;top:879px;width:199px;height:162px;background:linear-gradient(180deg,#4a7a28 0%,#6f8a4a 40%,#a89c84 80%,#b2a791 100%)" role="img" aria-label="Ivy covered stone wall"></div>
  <div class="abs tile tile-text" style="left:593px;top:879px;width:200px;height:162px;background:var(--orange)">
    <h3>ECO GARDENS</h3><div class="bar"></div>
    <p>Lorem Ipsum is simply dummy text of the printing and typesetting industry. Lorem Ipsum has been the industry's standard dummy text ever since the 1500s...</p>
  </div>
  <svg class="abs" style="left:686px;top:872px" width="14" height="8" viewBox="0 0 14 8"><path d="M0 8h14L7 1z" fill="#fe5722"/></svg>

  <h2 class="abs section-title" style="top:1060px"><span class="line"></span>BLOG<span class="line"></span></h2>

  <article class="abs post" style="left:106px">
    <div class="thumb" style="background:linear-gradient(180deg,#9a9890 0%,#7d7b74 60%,#2a2620 100%)" role="img" aria-label="Young seedling sprouting from dark soil"></div>
    <div class="meta"><span>&#9679; Super User</span><span>&#9635; December, 12 2018</span></div>
    <h4>Lorem Ipsum is simply dummy<br>text of the printing...</h4>
  </article>
  <article class="abs post" style="left:307px">
    <div class="thumb" style="background:linear-gradient(180deg,#d6e0e4 0%,#8a9a6a 45%,#7c6a48 100%)" role="img" aria-label="Thatched hut on a green hillside"></div>
    <div class="meta"><span>&#9679; Super User</span><span>&#9635; December, 12 2018</span></div>
    <h4>Lorem Ipsum is simply dummy<br>text of the printing...</h4>
  </article>
  <article class="abs post" style="left:505px">
    <div class="thumb" style="background:linear-gradient(135deg,#3f6a1a,#7a9a2a 45%,#2f4f14)" role="img" aria-label="Coffee cherries ripening on a branch"></div>
    <div class="meta"><span>&#9679; Super User</span><span>&#9635; December, 12 2018</span></div>
    <h4>Lorem Ipsum is simply dummy<br>text of the printing...</h4>
  </article>

  <footer class="abs footer"></footer>
  <div class="abs f-brand"><span class="dot"></span><span>TILLARD ENVIRONMENTAL PROJECTS</span></div>
  <span class="abs social" style="left:106px"></span>
  <span class="abs social" style="left:137px"></span>
  <span class="abs social" style="left:167px"></span>
  <span class="abs social" style="left:198px"></span>

  <h3 class="abs f-title" style="left:353px;top:1318px">Quick link</h3>
  <ul class="abs links">
    <li>HOME</li><li>WHO WE ARE</li><li>SERVICES</li><li>PRODUCTS</li><li>NEWS</li><li>CONTACT</li>
  </ul>

  <h3 class="abs f-title" style="left:522px;top:1318px">Our Newsletter:</h3>
  <div class="abs field-input" style="top:1347px">Name</div>
  <div class="abs field-input" style="top:1377px">Email</div>
  <div class="abs subscribe">Subscribe Newsletter</div>

  <div class="abs copy-line"></div>
  <p class="abs copyright">Copyright 2019 | Tillard Environmental Project</p>
</div>
</body>
</html>
```